Modernize and improve usability of our webpage www.lernwandel.ch (4 languages, mostly static content)

Need to modernize and freshen up the webpages of our association: www.lernwandel.ch We offer apprenticeship exchanges within Switzerland and abroad. Young people can inform and enroll online. We do the matchmaking with work locations and organize logistics, stay overs etc.
The webpage needs to be in 4 languages (German, French, Italian and English). The main pages will be:
- Landing page: what we do, targeted to our apprentices / young people who enroll for the stages.
- Sup-Page: Registration form for interested apprentices to sign up for the program
- Sub-Page "Company", the firms who would like to send their apprentices on a internship and info on how to join the program
- Sub-Page "Host Family", private people who would be interested in hosting the apprentices (for free) during the stages. Find out about the reqiurements for the host families
- Sub-Page "About Us", who we are, executive team, board of director, our sponsor "Corvina Circle Switzerland"
- Footer: contact (E-Mail, Telephone, WhatsApp), Bank details (IBAN Number), Partnerlogo of Corvina-Circle (see uploaded jpg), Social-Media Links (Facebook, LinkedIn)

Target Market(s)

Young people looking for a "apprenticeship" stage within Switzerland or going from Switzerland abroad

Industry/Entity Type

Apprenticeships: cooks, builders, craftsman, office support, etc.

Font styles to use
Other font styles liked:
• Lato (sans serif)

Requirements
Must have
• use colors shown on uploaded PDF-Slides: Make the BLUE the MAIN color, the ORANGE as a secondary color
Nice to have
• Forms using e.g. google forms or survey-monkey forms (external links, no code). Matching & appealing visuals showing young apprentices (can use stock photos)

```html
<!DOCTYPE html>
<html lang="en">
<head>
<meta charset="utf-8">
<title>Lernwandel – Apprenticeship Exchanges</title>
<link href="https://fonts.googleapis.com/css2?family=Lato:wght@300;400;700;900&display=swap" rel="stylesheet">
<style>
:root{
  --blue:#1e8af2;
  --blue-deep:#0b4f9e;
  --navy:#0a3f86;
  --orange:#ff6a00;
  --ink:#1c3a66;
  --muted:#8a97a8;
  --white:#ffffff;
  --page:#f4f6f9;
}
*{box-sizing:border-box;margin:0;padding:0}
html,body{width:1200px;height:4332px;overflow:hidden;background:var(--page);font-family:'Lato',sans-serif;color:var(--ink)}
.page{width:1200px;height:4332px;background:var(--white);position:relative;overflow:hidden}
a{color:inherit;text-decoration:none}
.btn{display:inline-block;font-weight:700;font-size:13px;padding:11px 26px;border-radius:3px}
.btn-blue{background:var(--blue);color:var(--white)}
.btn-orange{background:var(--orange);color:var(--white)}
.btn-white{background:var(--white);color:var(--blue)}
.eyebrow{font-size:13px;font-weight:700;color:var(--orange)}
.ph{display:block}

/* header */
.topbar{position:absolute;right:70px;top:10px;width:470px;height:26px;background:var(--orange);color:var(--white);font-size:11px;display:flex;justify-content:flex-end;align-items:center;gap:18px;padding-right:20px}
.nav{position:absolute;top:46px;left:70px;right:70px;height:60px;display:flex;align-items:center}
.logo{font-size:44px;font-weight:900;color:var(--blue);letter-spacing:-1px;margin-right:70px}
.nav ul{display:flex;gap:26px;list-style:none;font-size:12px;color:var(--ink);flex:1}
.nav li.active{color:var(--orange);font-weight:700}
.nav .login{color:var(--orange);font-size:12px;font-weight:700;margin-right:18px}
.nav .lang{background:#9fb1c6;color:var(--white);font-size:12px;padding:10px 18px;border-radius:3px;margin-left:8px}

/* hero */
.hero{position:absolute;top:120px;left:0;width:1200px;height:420px}
.hero-text{position:absolute;top:110px;width:100%;text-align:center;color:var(--white)}
.hero-text h1{font-weight:300;font-size:38px;line-height:1.2}
.hero-text h1 b{font-weight:700}
.hero-text .btn{margin-top:24px}

/* what we do */
.what{position:absolute;top:560px;left:0;width:1200px;height:470px}
.what-copy{position:absolute;left:125px;top:200px;width:320px}
.what-copy h2{font-weight:400;font-size:19px;line-height:1.45;margin:14px 0 30px}
.trade{position:absolute;width:182px;height:200px;border-radius:4px;overflow:hidden;background:linear-gradient(160deg,#6aa2d8,#1e6fc6)}
.trade span{position:absolute;bottom:22px;width:100%;text-align:center;color:var(--white);font-weight:700;font-size:14px}

/* companies */
.companies{position:absolute;top:1030px;left:0;width:1200px;height:700px}
.companies-head{position:absolute;top:120px;width:100%;text-align:center;color:var(--white)}
.companies-head .eyebrow{color:var(--white)}
.companies-head h2{font-weight:400;font-size:22px;line-height:1.35;margin-top:14px}
.co-grid{position:absolute;top:240px;left:125px;width:950px;display:flex;justify-content:space-between}
.co{width:300px;color:var(--white);text-align:center}
.co .ph{height:185px;border-radius:3px}
.co h3{font-size:15px;font-weight:700;margin:20px 0 10px}
.co p{font-size:11px;line-height:1.6;opacity:.9;padding:0 30px}
.companies .btn{position:absolute;top:560px;left:50%;transform:translateX(-50%)}

/* profit / costs */
.split{position:absolute;top:1730px;left:0;width:1200px;height:300px}
.icon-badge{position:absolute;top:-40px;width:92px;height:92px;border-radius:50%;background:var(--white);box-shadow:0 6px 18px rgba(10,63,134,.15);display:flex;align-items:center;justify-content:center}
.col{position:absolute;top:70px;width:330px;text-align:center}
.col h3{font-size:22px;font-weight:700;margin-bottom:18px}
.col p{font-size:11px;line-height:1.75;color:var(--muted)}
.divider{position:absolute;left:600px;top:90px;width:1px;height:160px;background:#d6dde6}
.split .btn{position:absolute;top:290px;left:50%;transform:translateX(-50%)}

/* host family */
.host{position:absolute;top:2070px;left:0;width:1200px;height:640px}
.host-copy{position:absolute;left:200px;top:200px;width:350px;color:var(--white)}
.host-copy .eyebrow{color:var(--white)}
.host-copy h2{font-weight:400;font-size:22px;line-height:1.4;margin:14px 0 20px}
.host-copy p{font-size:11px;line-height:1.7;margin-bottom:26px}
.host-photo{position:absolute;left:612px;top:150px;width:390px;height:390px;border-radius:50% 50% 50% 6%;background:linear-gradient(150deg,#e9d6c0,#b98760)}

/* about */
.about{position:absolute;top:2740px;left:0;width:1200px;height:640px;text-align:center}
.about h2{font-weight:400;font-size:22px;line-height:1.4;margin:18px auto 20px;width:700px;color:var(--blue-deep)}
.about p.lead{font-size:11px;line-height:1.7;width:760px;margin:0 auto;color:var(--ink)}
.about .btn-discover{margin-top:24px}
.team{position:absolute;left:200px;top:310px;width:800px;height:260px}
.member{position:absolute;width:250px;height:160px;background:var(--orange);border-radius:3px;text-align:left;color:var(--white);padding:100px 0 0 25px}
.member .ph{position:absolute;top:-55px;left:55px;width:135px;height:135px;border-radius:50%;background:linear-gradient(160deg,#d7dde5,#8d9aab)}
.member h4{font-size:14px;font-weight:700}
.member small{font-size:10px;opacity:.9}
.about .btn-team{position:absolute;top:590px;left:50%;transform:translateX(-50%)}

/* partners */
.partners{position:absolute;top:3400px;left:200px;width:800px;height:110px;display:flex;justify-content:space-between}
.partner{width:148px;height:70px;border:1px solid #e6eaf0;border-radius:3px;display:flex;align-items:center;justify-content:center}
.partner i{display:block;width:90px;height:18px;border-radius:3px;background:#cfd6df}
.partner.named{font-size:16px;color:#97a3b2;gap:6px}
.partner.named b{width:20px;height:20px;border-radius:50%;background:#cfd6df;display:inline-block}
.dots{position:absolute;top:3495px;left:590px;display:flex;gap:6px}
.dots span{width:8px;height:8px;border-radius:50%;border:1px solid var(--blue)}
.dots span:first-child{background:var(--blue)}

/* apply */
.apply{position:absolute;top:3540px;left:0;width:1200px;height:350px}
.apply-copy{position:absolute;left:125px;top:105px;width:480px;color:var(--white)}
.apply-copy small{font-size:12px;font-weight:700}
.apply-copy h2{font-size:30px;line-height:1.22;font-weight:900;margin:20px 0 26px}
.apply-copy h2 span{font-weight:300}
.survey{position:absolute;left:640px;top:-40px;width:340px;height:340px;border-radius:50%;background:var(--orange);color:var(--white);padding:50px 60px 0}
.survey h3{font-size:19px;font-weight:300;text-align:center}
.survey h3 b{display:block;font-weight:400}
.survey p{font-size:11px;margin:18px 0 14px}
.survey label{display:flex;align-items:center;gap:10px;font-size:10px;margin-bottom:9px}
.survey label i{width:10px;height:10px;border:1px solid var(--white);border-radius:50%}
.survey label i.on{background:var(--white)}
.survey .btn{background:#ff8d3c;margin:12px 0 0 50px;padding:10px 38px}
.apply-person{position:absolute;left:930px;top:10px;width:180px;height:340px;border-radius:90px 90px 0 0;background:linear-gradient(170deg,#e8eef5,#aebdcd)}

/* footer */
.footer{position:absolute;top:3890px;left:0;width:1200px;height:442px;background:var(--navy);color:var(--white)}
.f-logo{position:absolute;left:125px;top:70px}
.f-logo strong{font-size:48px;font-weight:900;letter-spacing:-1px}
.f-logo p{font-size:10px;line-height:1.6;width:200px;margin-top:12px;opacity:.85}
.f-col{position:absolute;top:70px;font-size:11px}
.f-col h4{font-size:13px;font-weight:700;margin-bottom:22px}
.f-col li{list-style:none;margin-bottom:12px;display:flex;gap:10px;align-items:flex-start}
.f-col li svg{flex:none}
.f-links{display:grid;grid-template-columns:80px 90px;gap:10px 20px;font-size:9px}
.news input{width:255px;height:34px;border:0;border-radius:3px;padding:0 14px;font-family:inherit;font-size:10px;color:#6b7a8e}
.news .btn{margin-top:14px;padding:10px 26px;background:var(--blue)}
.f-bottom{position:absolute;left:125px;right:90px;top:340px;display:flex;align-items:center;font-size:9px}
.f-bottom .legal{margin-left:95px;display:flex;gap:14px}
.social{margin-left:135px;display:flex;gap:14px}
.social a{display:block;width:24px;height:24px;border-radius:50%;background:var(--blue)}
.social a + a{background:var(--orange)}
.sponsor{margin-left:160px;display:flex;align-items:center;gap:8px;font-size:20px;font-weight:700}
.sponsor b{width:22px;height:22px;border-radius:50%;background:#f4b52c;display:inline-block}
.totop{margin-left:auto}
</style>
</head>
<body>
<div class="page">

  <!-- header -->
  <div class="topbar"><span>Accommodation</span><span>|</span><span>Application form</span><span>|</span><span>Downloads</span><span>|</span><span>FAQs</span></div>
  <header class="nav">
    <div class="logo">lernwandel</div>
    <ul>
      <li class="active">Home</li><li>Companies</li><li>Host Family</li><li>About Us</li><li>Experience Reports</li><li>Contact Us</li>
    </ul>
    <span class="login">&#9679; Login</span>
    <a class="btn btn-blue">Apply Now!</a>
    <span class="lang">En &#9662;</span>
  </header>

  <!-- hero -->
  <section class="hero">
    <svg class="ph" width="1200" height="420" viewBox="0 0 1200 420" role="img" aria-label="Photo of apprentices working in a professional kitchen, blue tinted">
      <defs><linearGradient id="heroG" x1="0" y1="0" x2="1" y2="1"><stop offset="0" stop-color="#2a6cb6"/><stop offset="1" stop-color="#14488c"/></linearGradient></defs>
      <path d="M0 0H1200V395C1080 340 960 330 820 370 640 420 460 350 300 345 170 342 70 380 0 420Z" fill="url(#heroG)"/>
    </svg>
    <div class="hero-text">
      <h1>We offer <b>apprenticeship</b> exchanges within<br><b>Switzerland and abroad</b></h1>
      <a class="btn btn-orange">Contact Us Today</a>
    </div>
  </section>

  <!-- what we do -->
  <section class="what">
    <div class="what-copy">
      <div class="eyebrow">What We Do</div>
      <h2>Corvina Circle Switzerland/Liechtenstein mainly supports this program with the objective of promoting the mobility of apprentices</h2>
      <a class="btn btn-blue">Apply now!</a>
    </div>
    <div class="trade" style="left:556px;top:110px" role="img" aria-label="Photo of an apprentice cook preparing vegetables"><span>Cooks</span></div>
    <div class="trade" style="left:762px;top:0" role="img" aria-label="Photo of apprentice builders in hard hats"><span>Builders</span></div>
    <div class="trade" style="left:762px;top:225px" role="img" aria-label="Photo of a craftsman working with tools"><span>Craftsman</span></div>
    <div class="trade" style="left:968px;top:110px" role="img" aria-label="Photo of an office apprentice with a headset"><span>Office Support</span></div>
  </section>

  <!-- companies -->
  <section class="companies">
    <svg width="1200" height="700" viewBox="0 0 1200 700" style="position:absolute;top:0;left:0">
      <path d="M0 60C160 30 260 -10 420 20 600 55 760 110 940 80 1060 60 1140 30 1200 40V660C1100 630 980 600 820 620 640 645 520 690 360 670 200 650 90 630 0 650Z" fill="var(--blue)"/>
    </svg>
    <div class="companies-head">
      <div class="eyebrow">Companies</div>
      <h2>Every successful company builds on well educated and<br>motivated professionals.</h2>
    </div>
    <div class="co-grid">
      <div class="co">
        <div class="ph" role="img" aria-label="Photo of an illuminated arena building at night" style="background:linear-gradient(160deg,#7a2a2a,#d04a2a)"></div>
        <h3>Talbrunn Architektur AG</h3>
        <p>Our office Talbrunn Architektur AG, with headquarters in the Zurich region, is primarily active in the planning and...</p>
      </div>
      <div class="co">
        <div class="ph" role="img" aria-label="Photo of a cook flambéing in a steel kitchen" style="background:linear-gradient(160deg,#8a6a48,#e0902a)"></div>
        <h3>Ferrova AG</h3>
        <p>Die Firma Ferrova AG is a well known manufacturer of pressure vessel systems and glass linings for reactors, filters...</p>
      </div>
      <div class="co">
        <div class="ph" role="img" aria-label="Photo of a tailor measuring green fabric" style="background:linear-gradient(160deg,#e8e6df,#2d9a6e)"></div>
        <h3>Stoffwerk</h3>
        <p>Stoffwerk, the Swiss technical school for fashion and design, has a leading position in the Swiss fashion landscape.</p>
      </div>
    </div>
    <a class="btn btn-orange">View All Companies</a>
  </section>

  <!-- profit / costs -->
  <section class="split">
    <div class="icon-badge" style="left:349px"><svg width="40" height="40" viewBox="0 0 40 40" fill="none" stroke="var(--orange)" stroke-width="2"><rect x="10" y="12" width="18" height="22" rx="2"/><path d="M19 6v10M15 10l4-4 4 4M14 22h10M14 27h10"/></svg></div>
    <div class="icon-badge" style="left:759px"><svg width="40" height="40" viewBox="0 0 40 40" fill="none" stroke="var(--orange)" stroke-width="2"><circle cx="20" cy="14" r="7"/><path d="M6 30c5 0 8-4 14-4h8c2 0 2 3 0 3h-8M6 34h20l10-8"/></svg></div>
    <div class="col" style="left:230px">
      <h3>Profit</h3>
      <p>By taking part in this exchange programme, you broaden your professional as well as your personal horizon. Not only do you get to know a new environment, the challenge will be for you to adapt to it and demonstrate your high level of flexibility. You meet new people both at home and abroad and make new contacts, which are often maintained even after the exchange is over. Improve your language skills by using them in your daily life... [more]</p>
    </div>
    <div class="divider"></div>
    <div class="col" style="left:640px">
      <h3>Costs</h3>
      <p>Your training company continues paying your normal wage during the exchange. Wherever possible you live with a host family, where you have breakfast and dinner. Visits of the local Corvina Circle will provide financial support for any expenses arising from the accommodation. Only travel costs, lunch and any leisure activities need to be paid by yourself. The mediation and organization of the exchange is financed by the sponsors of the program.</p>
    </div>
    <a class="btn btn-blue">Apply now!</a>
  </section>

  <!-- host family -->
  <section class="host">
    <svg width="1200" height="640" viewBox="0 0 1200 640" style="position:absolute;top:0;left:0">
      <path d="M0 60C140 30 240 0 420 10 640 25 760 90 960 70 1080 58 1150 30 1200 35V560C1090 610 960 640 800 600 620 560 520 620 340 625 180 628 80 600 0 580Z" fill="var(--orange)"/>
    </svg>
    <div class="host-copy">
      <div class="eyebrow">Host Family</div>
      <h2>Lorem Ipsum is simply dummy text of the printing and typesetting industry.</h2>
      <p>It is a long established fact that a reader will be distracted by the readable content of a page when looking at its layout. The point of using Lorem Ipsum is that it has a more-or-less normal distribution of letters, as opposed to using 'Content here, content here...</p>
      <a class="btn btn-blue">About The Host Families</a>
    </div>
    <div class="host-photo" role="img" aria-label="Photo of a chef and young apprentices cooking together around a table"></div>
  </section>

  <!-- about -->
  <section class="about">
    <div class="eyebrow" style="color:var(--blue)">About Us</div>
    <h2>Lernwandel has been organizing the exchange of apprentices between different cultural and language regions within Switzerland as well as with other countries for more than 19 years.</h2>
    <p class="lead">Primary participants are all apprentices who are completing their basic vocational education and training.<br>Once registered for the exchange, Lernwandel will find a suitable exchange company and an appropriate accommodation, where the apprentice will go through an exchange of at least three weeks. Corvina Circle Switzerland/Liechtenstein mainly supports this program with the objective of promoting the mobility of apprentices.</p>
    <a class="btn btn-blue btn-discover">Discover More About</a>
    <div class="team">
      <div class="member" style="left:0;top:0"><div class="ph" role="img" aria-label="Portrait photo of Lea Brunner"></div><h4>Lea Brunner</h4><small>Co-Managing Director</small></div>
      <div class="member" style="left:275px;top:75px"><div class="ph" role="img" aria-label="Portrait photo of Sandra Kessler"></div><h4>Sandra Kessler</h4><small>Co-Managing Director</small></div>
      <div class="member" style="left:550px;top:0"><div class="ph" role="img" aria-label="Portrait photo of Giulia Morandi"></div><h4>Giulia Morandi</h4><small>Contact for Romandie</small></div>
    </div>
    <a class="btn btn-blue btn-team">View All Team</a>
  </section>

  <!-- partners -->
  <div class="partners">
    <div class="partner named">Corvina Circle <b></b></div>
    <div class="partner"><i></i></div>
    <div class="partner"><i></i></div>
    <div class="partner"><i></i></div>
    <div class="partner"><i style="width:50px"></i></div>
  </div>
  <div class="dots"><span></span><span></span></div>

  <!-- apply -->
  <section class="apply">
    <svg width="1200" height="350" viewBox="0 0 1200 350" style="position:absolute;top:0;left:0">
      <rect width="1200" height="350" fill="var(--blue)"/>
      <path d="M0 330C180 290 340 260 520 290 700 320 860 300 1020 270 1110 255 1170 265 1200 275V350H0Z" fill="var(--navy)"/>
    </svg>
    <div class="apply-copy">
      <small>Apply now!</small>
      <h2>Lernwandel organizes the exchange of apprentices <span>from different language and cultural areas in</span> Switzerland and abroad.</h2>
      <a class="btn btn-white">Apply now!</a>
    </div>
    <div class="survey">
      <h3>Employee engagement <b>Survey</b></h3>
      <p>I am inspired to meet my goals at work.</p>
      <label><i></i>Strongly agree</label>
      <label><i class="on"></i>Agree</label>
      <label><i></i>Neither agree nor disagree</label>
      <label><i></i>Disagree</label>
      <label><i></i>Strongly disagree</label>
      <a class="btn btn-orange">Next</a>
    </div>
    <div class="apply-person" role="img" aria-label="Photo of a smiling young man in a suit pointing toward the survey"></div>
  </section>

  <!-- footer -->
  <footer class="footer">
    <div class="f-logo">
      <strong>lernwandel</strong>
      <p>Lernwandel organizes the exchange of apprentices from different language and cultural areas in Switzerland and abroad.</p>
    </div>
    <div class="f-col" style="left:400px">
      <h4>Contact Us</h4>
      <ul>
        <li><svg width="12" height="12" viewBox="0 0 12 12"><circle cx="6" cy="6" r="6" fill="var(--orange)"/></svg>+41 (0) 31 555 01 20</li>
        <li><svg width="12" height="12" viewBox="0 0 12 12"><circle cx="6" cy="6" r="6" fill="var(--orange)"/></svg>+41 79 555 01 21</li>
        <li><svg width="12" height="12" viewBox="0 0 12 12"><rect x="1" y="2" width="10" height="8" rx="1" fill="var(--orange)"/></svg>info@lernwandel.ch</li>
        <li><svg width="12" height="14" viewBox="0 0 12 14"><path d="M6 0a5 5 0 0 1 5 5c0 4-5 9-5 9S1 9 1 5a5 5 0 0 1 5-5z" fill="var(--orange)"/></svg><span>Lernwandel<br>Seeweg 12, 3600 Thun</span></li>
      </ul>
    </div>
    <div class="f-col" style="left:610px">
      <h4>Quick Links</h4>
      <div class="f-links">
        <span>Home</span><span>Accommodation</span>
        <span>Companies</span><span>Application form</span>
        <span>Host Family</span><span>Downloads</span>
        <span>About Us</span><span>FAQs</span>
        <span>Experience Reports</span><span></span>
        <span>Contact Us</span><span></span>
      </div>
    </div>
    <div class="f-col news" style="left:818px">
      <h4>Subscribe Newsletter</h4>
      <input type="text" value="name@email.com" aria-label="Email address"><br>
      <a class="btn">Submit</a>
    </div>
    <div class="f-bottom">
      <span>© 2023 Lernwandel. All Rights Reserved.</span>
      <span class="legal"><span>Imprint</span><span>|</span><span>Privacy policy</span></span>
      <span class="social"><a aria-label="Social media link"></a><a aria-label="Social media link"></a></span>
      <span class="sponsor">Corvina Circle <b></b></span>
      <span class="totop"><svg width="18" height="20" viewBox="0 0 18 20"><path d="M9 0L18 20 9 14 0 20Z" fill="var(--blue)"/></svg></span>
    </div>
  </footer>

</div>
</body>
</html>
```